Solar appointment reminder card

We are looking for a new design for our appointment reminder card since we have changed our logo. The card should have the new logo along with space for the employee to hand write the customers appointment date, time, the employees name and phone number.
I've uploaded what our old basic appointment card looked like and our new logo.

The cards should be in a standard business card size and could be horizontal or vertical.

```html
<!DOCTYPE html>
<html lang="en">
<head>
<meta charset="utf-8">
<title>Sunvale Solar – Appointment Reminder Card</title>
<link rel="stylesheet" href="https://fonts.googleapis.com/css2?family=Montserrat:wght@600;700&family=Lato:wght@400&display=swap">
<style>
  :root {
    --page-bg: #d9d9d9;
    --card-white: #f4f4f4;
    --orange-deep: #e07a1c;
    --orange-mid: #ee9228;
    --orange-warm: #f2a83a;
    --gold-light: #f6c24a;
    --label-grey: #7a7a7a;
    --rule-grey: #8c8c8c;
  }
  * { box-sizing: border-box; margin: 0; padding: 0; }
  html, body {
    width: 1200px; height: 900px; overflow: hidden;
    background: var(--page-bg);
  }
  .card {
    position: absolute; left: 75px; top: 150px;
    width: 1050px; height: 600px;
    background: var(--card-white);
    overflow: hidden;
    box-shadow: 0 6px 24px rgba(0,0,0,0.18);
  }
  .card-waves { position: absolute; inset: 0; width: 100%; height: 100%; }

  .brand {
    position: absolute; left: 58px; top: 52px;
    display: flex; align-items: center; gap: 14px;
  }
  .brand-dot {
    width: 46px; height: 46px; border-radius: 50%;
    background: var(--gold-light);
  }
  .brand-name {
    font-family: "Montserrat", sans-serif; font-weight: 700;
    font-size: 34px; color: var(--orange-mid); letter-spacing: 0.5px;
  }

  .day-row {
    position: absolute; left: 110px; top: 160px; width: 820px;
    display: flex; justify-content: space-between;
  }
  .day {
    display: flex; align-items: center; gap: 8px;
    font-family: "Montserrat", sans-serif; font-weight: 600;
    font-size: 22px; color: var(--orange-mid);
  }
  .tick-box {
    width: 20px; height: 20px;
    border: 2px solid var(--orange-mid); border-radius: 4px;
  }

  .field-row {
    position: absolute; left: 110px;
    display: flex; align-items: flex-end; gap: 14px;
    font-family: "Lato", sans-serif; font-size: 24px; color: var(--label-grey);
  }
  .field-row.name { top: 220px; width: 820px; }
  .field-row.date-time { top: 280px; width: 860px; }
  .field-row.phone { top: 340px; width: 800px; }
  .write-line {
    flex: 1; border-bottom: 2px solid var(--rule-grey); margin-bottom: 6px;
  }
  .write-line.short { flex: 0 0 300px; }
  .write-line.time { flex: 0 0 200px; }
  .meridiem {
    display: flex; align-items: center; gap: 6px;
    font-family: "Montserrat", sans-serif; font-weight: 600;
    font-size: 20px; color: var(--label-grey);
  }
  .meridiem .tick-box { border-color: var(--label-grey); }
</style>
</head>
<body>
  <section class="card" aria-label="Appointment reminder card">
    <svg class="card-waves" viewBox="0 0 1050 600" preserveAspectRatio="none" aria-hidden="true">
      <defs>
        <linearGradient id="top-wave" x1="0" y1="0" x2="1" y2="0">
          <stop offset="0" stop-color="#ee9228"/>
          <stop offset="1" stop-color="#f0a030"/>
        </linearGradient>
        <linearGradient id="bottom-wave" x1="0" y1="1" x2="1" y2="0">
          <stop offset="0" stop-color="#d86a14"/>
          <stop offset="1" stop-color="#f2a83a"/>
        </linearGradient>
        <linearGradient id="bottom-wave-light" x1="0" y1="1" x2="1" y2="0">
          <stop offset="0" stop-color="#ee9228"/>
          <stop offset="1" stop-color="#f6c24a"/>
        </linearGradient>
      </defs>
      <path d="M370 0 C520 70 650 105 790 98 C910 92 1000 45 1050 0 Z" fill="url(#top-wave)"/>
      <path d="M560 0 C680 50 800 70 900 55 C970 45 1020 20 1050 0 Z" fill="#f6b640" opacity="0.55"/>
      <path d="M620 0 C720 30 820 40 910 25 C960 18 1010 8 1050 0 Z" fill="#e88a22" opacity="0.6"/>
      <path d="M0 585 C250 505 550 475 780 435 C950 405 1030 330 1050 250 L1050 600 L0 600 Z" fill="url(#bottom-wave)"/>
      <path d="M180 600 C430 540 760 500 900 440 C990 400 1040 340 1050 300 L1050 600 Z" fill="url(#bottom-wave-light)" opacity="0.7"/>
    </svg>

    <div class="brand">
      <span class="brand-dot"></span>
      <span class="brand-name">Sunvale Solar</span>
    </div>

    <div class="day-row">
      <span class="day">MON <span class="tick-box"></span></span>
      <span class="day">TUE <span class="tick-box"></span></span>
      <span class="day">WED <span class="tick-box"></span></span>
      <span class="day">THUR <span class="tick-box"></span></span>
      <span class="day">FRI <span class="tick-box"></span></span>
      <span class="day">SAT <span class="tick-box"></span></span>
    </div>

    <div class="field-row name">
      <span>Name</span><span class="write-line"></span>
    </div>
    <div class="field-row date-time">
      <span>Date</span><span class="write-line short"></span>
      <span>Time</span><span class="write-line time"></span>
      <span class="meridiem">AM <span class="tick-box"></span></span>
      <span class="meridiem">PM <span class="tick-box"></span></span>
    </div>
    <div class="field-row phone">
      <span>Phone No</span><span class="write-line"></span>
    </div>
  </section>
</body>
</html>
```